VORELLI Industrial Maintenance

I offer repair and maintenance services of industrial mechanics in Quebec. I would like a creation that reflects confidence, competence, professionalism and dynamism. I like the orange color and the blue color.

Target Market(s)

Industries and Manufacturing companies using industrial machinery for the manufacture of their products.

Industry/Entity Type

Manufacturing

Contact Information for Business Card

VORELLI Maintenance Industrielle
Tél: (450)-318-5907
Courriel: vorelli.mnt@brastomail.com

Font styles to use
Sans Serif

Colors
f78f20
0455a3

Requirements
Must have
• My company name: VORELLI Maintenance Industrielle My phone: (450) -318-5907 My email: vorelli.mnt@brastomail.com
Nice to have
• Integrate a representative logo of the mechanics (gears, mechanical parts)

```html
<!DOCTYPE html>
<html lang="fr">
<head>
<meta charset="utf-8">
<title>VORELLI Maintenance Industrielle – Carte d'affaires</title>
<link rel="stylesheet" href="https://fonts.googleapis.com/css2?family=Montserrat:wght@500;600;700&display=swap">
<style>
  :root {
    --blue: #2c4a9e;
    --brand-blue: #0455a3;
    --orange: #f78f20;
    --white: #ffffff;
    --backdrop: #2a2a2c;
  }
  html, body {
    margin: 0;
    padding: 0;
    width: 1200px;
    height: 905px;
    overflow: hidden;
    background: var(--backdrop);
    font-family: "Montserrat", Arial, sans-serif;
  }
  .card {
    position: absolute;
    left: 100px;
    top: 166px;
    width: 1000px;
    height: 572px;
    background: var(--white);
    border-radius: 30px;
    overflow: hidden;
  }
  .card-bands {
    position: absolute;
    inset: 0;
  }
  .brand {
    position: absolute;
    left: 0;
    right: 0;
    top: 140px;
    display: flex;
    align-items: center;
    justify-content: center;
    gap: 18px;
  }
  .brand-dot {
    width: 44px;
    height: 44px;
    border-radius: 50%;
    background: var(--orange);
  }
  .brand-name {
    color: var(--brand-blue);
    font-weight: 700;
    font-size: 40px;
    letter-spacing: 1px;
  }
  .holder {
    position: absolute;
    right: 540px;
    top: 382px;
    color: var(--white);
    text-align: right;
    white-space: nowrap;
  }
  .holder-name {
    font-weight: 600;
    font-size: 32px;
    letter-spacing: 2px;
    text-transform: uppercase;
    line-height: 1.1;
  }
  .holder-title {
    font-weight: 500;
    font-size: 17px;
    letter-spacing: 1.5px;
    text-transform: uppercase;
    margin-top: 4px;
  }
  .divider {
    position: absolute;
    left: 490px;
    top: 350px;
    width: 3px;
    height: 110px;
    background: var(--white);
  }
  .contacts {
    position: absolute;
    left: 525px;
    top: 350px;
    color: var(--white);
    font-weight: 500;
    font-size: 23px;
    letter-spacing: 0.5px;
    white-space: nowrap;
  }
  .contact-line {
    display: flex;
    align-items: center;
    gap: 14px;
    height: 52px;
  }
  .contact-icon {
    width: 34px;
    height: 34px;
    border-radius: 50%;
    background: var(--orange);
    display: flex;
    align-items: center;
    justify-content: center;
    flex: none;
  }
</style>
</head>
<body>
  <div class="card">
    <svg class="card-bands" width="1000" height="572" viewBox="0 0 1000 572" aria-hidden="true">
      <polygon points="0,305 1000,270 1000,500 0,500" fill="var(--blue)"/>
      <rect x="0" y="510" width="1000" height="62" fill="var(--orange)"/>
    </svg>

    <div class="brand">
      <span class="brand-dot"></span>
      <span class="brand-name">VORELLI Maintenance Industrielle</span>
    </div>

    <div class="holder">
      <div class="holder-name">Marc Dellaire</div>
      <div class="holder-title">Managing Director</div>
    </div>

    <div class="divider"></div>

    <div class="contacts">
      <div class="contact-line">
        <span class="contact-icon">
          <svg width="18" height="18" viewBox="0 0 24 24" aria-hidden="true">
            <path d="M6.6 10.8a15.1 15.1 0 0 0 6.6 6.6l2.2-2.2a1 1 0 0 1 1-.25 11.4 11.4 0 0 0 3.6.57 1 1 0 0 1 1 1V20a1 1 0 0 1-1 1A17 17 0 0 1 3 4a1 1 0 0 1 1-1h3.5a1 1 0 0 1 1 1c0 1.25.2 2.45.57 3.57a1 1 0 0 1-.25 1z" fill="var(--white)"/>
          </svg>
        </span>
        <span>(450)-318-5907</span>
      </div>
      <div class="contact-line">
        <span class="contact-icon">
          <svg width="18" height="14" viewBox="0 0 24 18" aria-hidden="true">
            <rect x="1" y="1" width="22" height="16" rx="2" fill="var(--white)"/>
            <path d="M2 2l10 8 10-8" fill="none" stroke="var(--orange)" stroke-width="2"/>
          </svg>
        </span>
        <span>vorelli.mnt@brastomail.com</span>
      </div>
    </div>
  </div>
</body>
</html>
```